Web Design Project

I have a website which looks dull and uninteresting. I'd like to apply a fresh and clean look to it, which better reflects the quality of the service I sell.The website address is http://www.brightquillpages.co.uk.

Target Market(s)

Financial advisers (financially sophisticated individuals)

Industry/Entity Type

It Service

Requirements
Should not have
• Please do not use obvious but irrelevant and boring imagery such as banks, pages from the MQ, money, books or libraries. Prefer slick relevant graphics and crisp typography.

```html
<!DOCTYPE html>
<html lang="en">
<head>
<meta charset="utf-8">
<title>Bright Quill Pages.co.uk – Words to use as you please</title>
<link rel="stylesheet" href="https://fonts.googleapis.com/css2?family=Arimo:ital,wght@0,400;0,700;1,400&family=Jost:wght@400;500;700&display=swap">
<style>
:root{
  --bar-grey:#e6e7e8;
  --footer-grey:#5f5f61;
  --orange:#ff6a00;
  --red:#ee3535;
  --ink:#111;
  --text-grey:#555;
  --olive:#8a8a6d;
  --muted:#a9a9a9;
  --white:#fff;
  --cream:#f6ece4;
}
*{box-sizing:border-box;margin:0;padding:0}
html,body{width:1200px;height:889px;overflow:hidden;background:var(--white)}
body{position:relative;font-family:"Arimo",Arial,sans-serif;color:var(--ink)}
a{color:inherit;text-decoration:none}

.utility-bar{position:absolute;left:0;top:0;width:1200px;height:36px;background:var(--bar-grey);font-size:12px;letter-spacing:.4px;color:#333}
.utility-bar .date{position:absolute;left:232px;top:16px}
.utility-bar .time{position:absolute;left:410px;top:16px}
.utility-bar .help-links{position:absolute;right:218px;top:16px;word-spacing:3px}

.brand{position:absolute;left:222px;top:66px;display:flex;align-items:center;gap:10px}
.brand-square{width:22px;height:22px;background:var(--orange);border-radius:3px}
.brand-name{font-family:"Jost",sans-serif;font-weight:500;font-size:30px;color:var(--orange);letter-spacing:-.3px}
.tagline{position:absolute;left:390px;top:103px;font-size:12px;color:#222}

.member-login{position:absolute;left:700px;top:58px;width:281px;height:76px}
.member-login .label{position:absolute;right:202px;top:14px;text-align:right;font-size:11px;line-height:14px;color:#333}
.member-login .field{position:absolute;left:90px;width:191px;height:24px;border:1px solid #d6d6d6;font-family:"Arimo",sans-serif;font-style:italic;font-size:9px;color:#aaa;padding:4px 7px;line-height:15px}
.member-login .field.user{top:0}
.member-login .field.pass{top:27px}
.member-login .forgot{position:absolute;left:91px;top:62px;font-size:9px;font-style:italic;letter-spacing:.5px;color:#555}
.btn-small{position:absolute;left:234px;top:57px;width:47px;height:17px;border:1px solid #333;border-radius:4px;background:linear-gradient(#eee,#d6d6d6);font-size:11px;text-align:center;line-height:15px;color:#222}

.main-nav{position:absolute;left:222px;top:159px;height:27px;display:flex;gap:3px}
.main-nav a{display:block;height:27px;background:var(--bar-grey);border-radius:6px 6px 0 0;font-size:12px;color:#222;text-align:center;line-height:29px}
.main-nav a.active{background:var(--orange);color:var(--white)}

.promo{position:absolute;left:222px;top:185px;width:758px;height:208px;background:linear-gradient(var(--orange),var(--red));border-radius:0 0 14px 14px;color:var(--white)}
.promo .arrow{position:absolute;top:74px;width:30px;height:31px;background:var(--white);border-radius:4px}
.promo .arrow.prev{left:30px}
.promo .arrow.next{left:697px}
.promo .price{position:absolute;left:154px;top:34px;font-family:"Jost",sans-serif;font-weight:700;font-size:76px;line-height:90px;color:var(--ink);letter-spacing:-2px}
.promo .headline{position:absolute;left:295px;top:46px;font-weight:700;font-size:35px;line-height:37px;color:var(--cream)}
.promo .details{position:absolute;left:161px;top:136px;font-family:"Jost",sans-serif;font-size:18px;line-height:21px}
.promo .btn-access{position:absolute;left:502px;top:150px;width:80px;height:30px;border:1px solid #222;border-radius:5px;background:linear-gradient(#f2f2f2,#d3d3d3);color:#333;font-size:18px;text-align:center;line-height:28px}

.intro{position:absolute;left:246px;top:410px;width:556px}
.intro h1{font-family:"Jost",sans-serif;font-weight:400;font-size:21px;line-height:24px;color:var(--red);margin-bottom:15px}
.intro p{font-size:13px;line-height:14.6px;margin-left:-2px;margin-bottom:14px;width:520px}
.intro p.soft{color:var(--text-grey)}
.intro .more{margin-top:20px;font-size:13px;letter-spacing:.4px;color:var(--olive);word-spacing:2px}

.divider{position:absolute;left:807px;top:405px;height:330px;border-left:1px dotted #333}

.side-nav{position:absolute;left:822px;top:424px;list-style:none}
.side-nav li{font-size:10px;line-height:20.4px;color:var(--olive)}
.social{position:absolute;left:829px;top:702px;display:flex;gap:9px}
.social span{width:24px;height:24px;border-radius:50%;background:#444;border:1px solid #222}

.article-band{position:absolute;left:0;top:745px;width:1200px;height:50px;background:var(--bar-grey);font-size:12px;color:#888;text-align:center;line-height:56px;padding-left:2px;word-spacing:1px}
.site-footer{position:absolute;left:0;top:795px;width:1200px;height:94px;background:var(--footer-grey);text-align:center}
.site-footer .footer-nav{margin-top:16px;font-size:13px;color:var(--white)}
.site-footer .copyright{margin-top:4px;font-size:12px;color:var(--muted)}
</style>
</head>
<body>

<header class="utility-bar">
  <span class="date">Thursday, August 18, 2011</span>
  <span class="time">12:29</span>
  <nav class="help-links"><a href="#">Support</a> | &nbsp;<a href="#">FAQ</a> &nbsp;| <a href="#">Sitemap</a></nav>
</header>

<a class="brand" href="http://www.brightquillpages.co.uk"><span class="brand-square"></span><span class="brand-name">BrightQuillPages.co.uk</span></a>
<div class="tagline">Words to use as you please</div>

<form class="member-login">
  <div class="label">Member<br>Login</div>
  <div class="field user">Username</div>
  <div class="field pass">Password</div>
  <span class="forgot">Forgotten your password?</span>
  <span class="btn-small">Login</span>
</form>

<nav class="main-nav">
  <a class="active" href="#" style="width:89px">Home</a>
  <a href="#" style="width:88px">A-Z Articles</a>
  <a href="#" style="width:104px">Inheritance Tax</a>
  <a href="#" style="width:85px">Insurances</a>
  <a href="#" style="width:85px">Mortgages</a>
  <a href="#" style="width:58px">Other</a>
  <a href="#" style="width:86px">Retirement</a>
  <a href="#" style="width:141px">Saving &amp; Investment</a>
</nav>

<section class="promo">
  <span class="arrow prev"><svg width="30" height="31" viewBox="0 0 30 31"><path d="M18 9 L11 15.5 L18 22" fill="none" stroke="#111" stroke-width="3.5" stroke-linecap="round" stroke-linejoin="round"/></svg></span>
  <div class="price">£49</div>
  <div class="headline">Unlimited access<br>to all our articles...</div>
  <div class="details">£49 a year, at least 131 articles<br>(plus free guides as they're published)</div>
  <a class="btn-access" href="#">Access</a>
  <span class="arrow next"><svg width="30" height="31" viewBox="0 0 30 31"><path d="M12 9 L19 15.5 L12 22" fill="none" stroke="#111" stroke-width="3.5" stroke-linecap="round" stroke-linejoin="round"/></svg></span>
</section>

<main class="intro">
  <h1>131 ready-written, copyright-free personal financial planning articles which you can use or adapt in almost any way you want and for as long as you want.</h1>
  <p>Donec vitae massa sit amet lectus condimentum aliquam vestibulum tempor nunc vel mi laoreet nec condimentum mauris convallis. Praesent lobortis, lectus a viverra faucibus, urna turpis sodales purus, magnaorem ipsum dolor ser adipiscing elit sed diam nonummy nibh euismod sit amet ornare urna augue ut mauris.</p>
  <p>Cras placerat, risus ac porta auctor, dui neque varius libero, sed rutrum diam mauris sed lorem. Ut at risus eu dui pretium sodales proin fermentum condimentum eros quis tincidunt fraesent eleifend tempor nisi, in adipiscing felis molestie vitae. Sed et massa justo. Pellentesque turpis lorem, ornare sit amet vulputate at, consectetur.</p>
  <p class="soft">Vitae massa sit amet lectus condimentum aliquam vestibulum tempor nunc vel mi laoreet nec condimentum mauris convallis. Praesent lobortis, lectus a viverra faucibus, urna turpis sodales purus, magnaorem ipsum dolor ser adipiscing elit sed diam nonummy nibh euismod sit amet ornare urna augue ut mauris.</p>
  <div class="more"><a href="#">View our library</a> &nbsp;| &nbsp;<a href="#">See samples of our articles</a></div>
</main>

<div class="divider"></div>

<ul class="side-nav">
  <li>Home</li>
  <li>Samples</li>
  <li>The people who write the articles</li>
  <li>Please don't lift our words</li>
  <li>A - Z of articles</li>
  <li>Enter the library</li>
  <li>Join the library here</li>
  <li>Some FAQs</li>
  <li>Contact us</li>
  <li>A few terms &amp; conditions</li>
  <li>A comment to make?</li>
  <li>A question to ask?</li>
  <li>Want something writing?</li>
</ul>
<div class="social"><span></span><span></span><span></span></div>

<div class="article-band">Why financial advice can never be free &nbsp;| &nbsp;What it takes to be a financial adviser &nbsp;| &nbsp;IHT Planning: A guessing and waiting game...</div>

<footer class="site-footer">
  <nav class="footer-nav">Home &nbsp;| &nbsp;A - Z Articles &nbsp;| &nbsp;Inheritance Tax &nbsp;| &nbsp;Insurances &nbsp;|Mortgages &nbsp;| &nbsp;Other &nbsp;| &nbsp;Retirement &nbsp;| &nbsp;Saving and Investment</nav>
  <div class="copyright">© 2011 &nbsp;All rights reserved. &nbsp;Bright Quill Pages.co.uk</div>
</footer>

</body>
</html>
```